Trovadel Ltda

Logo design focused on: - Construction of civil works - Electrical services - Metal structures - Equipment rental Tomas Ibarra Luque Manager trovadel.ltda@norvexmail.com 56 9 41827035 Quirobamba s / n, Tolvas, San Pedro de Atacama

Target Market(s)

Building

Colors
33a6d7
0292cd
33b8a4
0555a3

```html
<!DOCTYPE html>
<html lang="en">
<head>
<meta charset="utf-8">
<title>Trovadel Ltda – Business Card</title>
<link rel="stylesheet" href="https://fonts.googleapis.com/css2?family=Cinzel:wght@500&family=Open+Sans:wght@400;600&display=swap">
<style>
  :root {
    --backdrop: #2b2725;
    --card: #0d0d0e;
    --card-edge: #1c1c1e;
    --sky: #33a6d7;
    --azure: #0292cd;
    --teal: #33b8a4;
    --navy: #0555a3;
    --name-blue: #1f78d1;
    --text: #e6e6e6;
    --muted: #bfbfbf;
    --silver: #d4d4d6;
    --divider: #3a3a3d;
  }
  * { box-sizing: border-box; margin: 0; padding: 0; }
  html, body { width: 1200px; height: 900px; overflow: hidden; }
  body {
    background: var(--backdrop);
    font-family: "Open Sans", Arial, sans-serif;
    display: flex;
    align-items: center;
    justify-content: center;
    gap: 50px;
  }
  .card {
    width: 540px;
    height: 310px;
    background: var(--card);
    border: 1px solid var(--card-edge);
    border-radius: 3px;
    box-shadow: 0 12px 30px rgba(0,0,0,.45);
    position: relative;
  }

  /* Front */
  .card-front { display: flex; align-items: center; }
  .brand-block {
    width: 230px;
    display: flex;
    flex-direction: column;
    align-items: center;
    gap: 14px;
  }
  .brand-dot {
    width: 120px; height: 120px;
    border-radius: 50%;
    background: var(--azure);
  }
  .brand-name-front {
    font-family: "Cinzel", Georgia, serif;
    font-weight: 500;
    font-size: 17px;
    color: var(--text);
    letter-spacing: 1px;
  }
  .front-divider {
    width: 1px; height: 150px;
    background: var(--divider);
  }
  .contact-block { padding-left: 26px; color: var(--text); }
  .person-name {
    font-family: "Cinzel", Georgia, serif;
    font-weight: 500;
    font-size: 19px;
    color: var(--name-blue);
    letter-spacing: .5px;
  }
  .person-role { font-size: 12px; margin-bottom: 14px; }
  .contact-line {
    display: flex; align-items: center; gap: 7px;
    font-size: 13px; line-height: 1.6;
  }
  .contact-icon {
    width: 14px; height: 14px; border-radius: 50%;
    background: var(--name-blue);
    display: inline-flex; align-items: center; justify-content: center;
    flex: none;
  }
  .address { font-size: 13px; line-height: 1.5; margin-top: 12px; }

  /* Back */
  .card-back { padding: 70px 50px 0 70px; }
  .brand-row { display: flex; align-items: center; gap: 16px; }
  .brand-seal {
    width: 58px; height: 58px; border-radius: 50%;
    background: var(--silver);
  }
  .brand-name-back {
    font-family: "Cinzel", Georgia, serif;
    font-weight: 500;
    font-size: 34px;
    color: var(--silver);
    letter-spacing: 2px;
  }
  .back-rule {
    height: 1px; background: var(--navy);
    margin: 40px 0 18px;
  }
  .services {
    list-style: none;
    display: grid;
    grid-template-columns: 1fr 1fr;
    gap: 4px 20px;
    color: var(--text);
    font-size: 14px;
  }
  .services li { display: flex; align-items: center; gap: 8px; }
  .services li::before {
    content: ""; width: 8px; height: 8px; border-radius: 50%;
    background: var(--teal); flex: none;
  }
</style>
</head>
<body>
  <section class="card card-front">
    <div class="brand-block">
      <div class="brand-dot"></div>
      <div class="brand-name-front">Trovadel Ltda</div>
    </div>
    <div class="front-divider"></div>
    <div class="contact-block">
      <h1 class="person-name">TOMAS IBARRA LUQUE</h1>
      <p class="person-role">Director</p>
      <p class="contact-line">
        <span class="contact-icon">
          <svg width="8" height="8" viewBox="0 0 10 10"><path d="M2 1 L4 3 L3 4 Q4.5 6 6 7 L7 6 L9 8 L8 9.5 Q3 9 0.5 2 Z" fill="#0d0d0e"/></svg>
        </span>56 9 41827035
      </p>
      <p class="contact-line">
        <span class="contact-icon">
          <svg width="8" height="8" viewBox="0 0 10 10"><rect x="0.5" y="2" width="9" height="6" fill="none" stroke="#0d0d0e" stroke-width="1.2"/><path d="M0.5 2 L5 5.5 L9.5 2" fill="none" stroke="#0d0d0e" stroke-width="1.2"/></svg>
        </span>trovadel.ltda@norvexmail.com
      </p>
      <p class="address">Quirobamba s / n, Tolvas,<br>San Pedro de Atacama</p>
    </div>
  </section>

  <section class="card card-back">
    <div class="brand-row">
      <div class="brand-seal"></div>
      <div class="brand-name-back">Trovadel Ltda</div>
    </div>
    <div class="back-rule"></div>
    <ul class="services">
      <li>Construction of Civil Works</li>
      <li>Metal Structures</li>
      <li>Electrical Services</li>
      <li>Equipment Rental</li>
    </ul>
  </section>
</body>
</html>
```